Korvel Professional Services Website

Small website for company presence and information. Company is an IT/Telecom services company. We provide presales and installation services. Included are various company logos including color levels. Site doesn't have to use these exact colors in the logos, but should be complimentary if using different colors. It should have a professional business appearance.
Updates

My apologies for not being more responsive on the designs that have been submitted. I will be narrowing down the submissions and providing additional feedback next week. Thank you for your patience.

Project Deadline Extended
Reason: Sorry again for delays on picking designs. Work has me very busy and I've just not had the time to devote to this project. I am extending the design deadline for a few more days to give me time to make my final decisions. Thank you all for your patience. Stay tuned....

Target Market(s)

Telecom sales companies that sell Quenti telecom products.

Industry/Entity Type

Professional Service

Coding

Coded - Design and coding required

Number of Pages Required

5+ page

Font styles to use
Sans Serif

Colors
3276b5
0355a3
85abd2
85cae6
33a6d7
0692cd
ffffff

Requirements
Must have
• Professional design reflective of IT/Telecom business. A good reference website would be: http://www.lorbextech.example/. Looking for something similar in function and presence.
Nice to have
• Rolling photos highlighting our services. Traditional navigation across the top of all pages.
Should not have
• No motion video, flashy presentation or overly confused interface.

```html
<!DOCTYPE html>
<html lang="en">
<head>
<meta charset="utf-8">
<title>Korvel Professional Services</title>
<link href="https://fonts.googleapis.com/css2?family=Open+Sans:wght@400;600;700&family=Bebas+Neue&display=swap" rel="stylesheet">
<style>
:root{
  --blue:#0355a3;
  --blue-mid:#3276b5;
  --sky:#2ea3f2;
  --ink:#333333;
  --text:#666666;
  --grey-bg:#ebebeb;
  --field:#e6e6e6;
  --dark:#000000;
  --footer:#222222;
  --white:#ffffff;
}
*{box-sizing:border-box;margin:0;padding:0}
html,body{width:1200px;height:3020px;overflow:hidden}
body{position:relative;font-family:"Open Sans",Arial,sans-serif;color:var(--text);background:var(--white)}
.abs{position:absolute}

/* header */
.site-header{left:0;top:0;width:1200px;height:68px;background:var(--white);border-bottom:1px solid #eee}
.brand{left:146px;top:16px;display:flex;align-items:center;gap:10px}
.brand-mark{width:30px;height:30px;background:var(--blue);border-radius:50%}
.brand-name{font-weight:700;font-size:22px;color:var(--blue);line-height:1}
.brand-sub{font-size:8px;color:var(--blue);letter-spacing:1.5px;font-weight:600;margin-top:3px}
.main-nav{right:172px;top:25px;display:flex;gap:24px;font-size:12px;font-weight:400;color:#555}
.main-nav .active{color:var(--sky)}
.search-icon{right:150px;top:26px}

/* hero */
.hero{left:0;top:88px;width:1200px;height:420px;overflow:hidden}
.hero-photo{left:0;top:0;width:1200px;height:420px;background:linear-gradient(90deg,#151515 0%,#2c2c2c 35%,#242424 62%,#3a2a1e 80%,#1a2030 100%)}
.hero-title{left:86px;top:286px;font-family:"Bebas Neue",Impact,sans-serif;font-weight:400;font-size:50px;line-height:1;color:var(--white);white-space:nowrap}
.hero-sub{left:188px;top:356px;font-size:19px;color:var(--white)}
.slide-arrow{top:286px;width:26px;height:26px;border-radius:50%;background:rgba(255,255,255,.85);display:flex;align-items:center;justify-content:center}

/* about */
.about{left:0;top:528px;width:1200px;height:402px;background:linear-gradient(135deg,#ffffff 0%,#ededed 40%,#f8f8f8 70%,#e4e4e4 100%)}
.section-title{font-size:28px;font-weight:600;color:#555;text-transform:uppercase}
.section-title b{color:var(--blue);font-weight:700}
.about .section-title{position:absolute;left:145px;top:64px}
.about-copy{position:absolute;left:145px;top:108px;width:908px;font-size:13.5px;line-height:26px;text-align:justify}
.about-copy p+p{margin-top:14px}
.read-more{position:absolute;right:147px;top:316px;font-size:13.5px;color:var(--sky)}

/* services */
.services{left:0;top:930px;width:1200px;height:682px;background:var(--grey-bg)}
.centered-title{position:absolute;left:0;width:1200px;text-align:center}
.dotted-rule{position:absolute;left:145px;width:910px;border-top:2px dotted #999}
.service{position:absolute;width:300px;text-align:center;font-size:16px;color:#555;line-height:26px}
.service svg{display:block;margin:0 auto 18px}

/* trust */
.trust{left:0;top:1612px;width:1200px;height:506px;background:var(--white)}
.trust-item{position:absolute;width:420px;display:flex;gap:14px}
.trust-icon{flex:none;width:56px;height:56px;border-radius:50%;background:var(--blue);display:flex;align-items:center;justify-content:center}
.trust-item h3{font-size:14.5px;font-weight:400;color:#444;margin-top:4px}
.trust-item p{font-size:11.5px;line-height:19px;color:#777}

/* approach */
.approach{left:0;top:2118px;width:1200px;height:450px;background:linear-gradient(160deg,#000 0%,#000 55%,#08103a 75%,#1a2a8a 85%,#000 100%)}
.approach-copy{position:absolute;left:145px;top:68px;width:430px;color:var(--white);font-size:11.5px;line-height:20px;text-align:justify}
.approach-copy .lead{font-size:15.5px;line-height:25px;margin-bottom:8px}
.approach-copy ul{padding-left:14px}
.approach-copy li{margin-bottom:10px}
.approach-photo{position:absolute;left:624px;top:58px;width:430px;height:226px;background:linear-gradient(180deg,#6a6a6a 0%,#bdbdbd 55%,#8a8a8a 100%)}
.btn-outline{position:absolute;left:770px;top:322px;width:138px;height:44px;border:2px solid var(--sky);color:var(--sky);font-size:15px;display:flex;align-items:center;justify-content:center}

/* contact */
.contact{left:0;top:2568px;width:1200px;height:410px;background:var(--white)}
.contact h2{position:absolute;left:145px;top:62px;font-size:21px;font-weight:400;color:#333}
.field{position:absolute;background:var(--field);font-size:11px;color:#999;padding:12px 14px}
.captcha{position:absolute;left:376px;top:298px;line-height:40px;font-size:12px;color:#555}
.captcha-box{position:absolute;left:426px;top:298px;width:40px;height:40px;background:var(--field)}
.submit{position:absolute;left:480px;top:298px;width:94px;height:40px;border:2px solid var(--sky);color:var(--sky);font-size:15px;display:flex;align-items:center;justify-content:center}
.testimonial{position:absolute;left:624px;top:122px;width:430px;height:166px;background:#f2f2f2}
.quote-mark{position:absolute;left:199px;top:-16px;width:32px;height:32px;border-radius:50%;background:#f2f2f2;font-size:26px;font-weight:700;color:#444;text-align:center;line-height:38px}
.avatar{position:absolute;left:26px;top:30px;width:76px;height:76px;border-radius:50%;background:linear-gradient(135deg,#5a4a3c,#2a221c)}
.testimonial blockquote{position:absolute;left:126px;top:28px;width:280px;font-size:11.5px;line-height:19px;color:#666}
.testimonial blockquote b{color:#333}
.testimonial cite{position:absolute;left:126px;top:112px;font-style:normal;font-size:11.5px;line-height:19px;color:#666}
.testimonial cite b{color:#333}

/* footer */
.site-footer{left:0;top:2978px;width:1200px;height:42px;background:var(--footer)}
.social{position:absolute;right:150px;top:12px;display:flex;gap:22px}
.social span{width:18px;height:18px;border-radius:50%;background:#666}
</style>
</head>
<body>

<header class="site-header abs">
  <div class="brand abs">
    <span class="brand-mark"></span>
    <div><div class="brand-name">KORVEL</div><div class="brand-sub">PROFESSIONAL SERVICES</div></div>
  </div>
  <nav class="main-nav abs">
    <span class="active">Home</span><span>Company</span><span>About Us</span><span>What We Do?</span><span>Portfolio</span><span>Contact Us</span>
  </nav>
  <svg class="search-icon abs" width="14" height="14" viewBox="0 0 14 14"><circle cx="8" cy="6" r="4.5" fill="none" stroke="#999" stroke-width="1.5"/><line x1="5" y1="9" x2="1" y2="13" stroke="#999" stroke-width="1.5"/></svg>
</header>

<section class="hero abs">
  <div class="hero-photo abs" role="img" aria-label="Dark photo of a hand touching floating digital communication icons"></div>
  <h1 class="hero-title abs">GROW YOUR BUSINESS TO IT'S FULL POTENTIAL</h1>
  <p class="hero-sub abs">Let’s Find out How with our Marketing Formula....</p>
  <div class="slide-arrow abs" style="left:18px"><svg width="10" height="10" viewBox="0 0 10 10"><path d="M7 1 L3 5 L7 9" fill="none" stroke="#222" stroke-width="2"/></svg></div>
  <div class="slide-arrow abs" style="right:18px"><svg width="10" height="10" viewBox="0 0 10 10"><path d="M3 1 L7 5 L3 9" fill="none" stroke="#222" stroke-width="2"/></svg></div>
</section>

<section class="about abs">
  <h2 class="section-title"><b>About</b> Korvel</h2>
  <div class="about-copy">
    <p>Lorem ipsum dolor sit amet, consectetuer adipiscing elit. Phasellus hendrerit. Pellentesque aliquet nibh nec urna. In nisi neque, aliquet vel, dapibus id, mattis vel, nisi. Sed pretium, ligula sollicitudin laoreet viverra, tortor libero sodales leo, eget blandit nunc tortor eu nibh. Nullam mollis. Ut justo. Suspendisse potenti.</p>
    <p>Sed egestas, ante et vulputate volutpat, eros pede semper est, vitae luctus metus libero eu augue. Morbi purus libero, faucibus adipiscing, commodo quis, gravida id, est. Sed lectus. Praesent elementum hendrerit tortor. Sed semper lorem at felis. Vestibulum volutpat, lacus a ultrices sagittis, mi neque euismod dui, eu pulvinar nunc sapien ornare nisl. Phasellus pede arcu, dapibus eu, fermentum et, dapibus sed, urna.</p>
  </div>
  <a class="read-more">Read More</a>
</section>

<section class="services abs">
  <h2 class="section-title centered-title" style="top:46px"><b>Our</b> Services</h2>
  <div class="dotted-rule" style="top:104px"></div>

  <div class="service" style="left:126px;top:154px">
    <svg width="124" height="124" viewBox="0 0 124 124"><path d="M62 4 A58 58 0 0 0 62 120" fill="none" stroke="#0355a3" stroke-width="6" stroke-dasharray="8 6"/><path d="M62 4 A58 58 0 0 1 62 120" fill="none" stroke="#666" stroke-width="5"/><rect x="42" y="66" width="8" height="18" fill="#0355a3"/><rect x="54" y="58" width="8" height="26" fill="#0355a3"/><rect x="66" y="50" width="8" height="34" fill="#0355a3"/><rect x="78" y="42" width="8" height="42" fill="#0355a3"/><polyline points="40,60 58,46 70,50 86,34" fill="none" stroke="#0355a3" stroke-width="3"/></svg>
    Sales and Marketing Consulting
  </div>
  <div class="service" style="left:450px;top:154px">
    <svg width="124" height="124" viewBox="0 0 124 124"><path d="M62 4 A58 58 0 0 0 62 120" fill="none" stroke="#0355a3" stroke-width="6" stroke-dasharray="8 6"/><path d="M62 4 A58 58 0 0 1 62 120" fill="none" stroke="#666" stroke-width="5"/><circle cx="58" cy="56" r="14" fill="none" stroke="#0355a3" stroke-width="4" stroke-dasharray="5 3"/><circle cx="58" cy="56" r="7" fill="none" stroke="#0355a3" stroke-width="3"/><line x1="68" y1="66" x2="82" y2="80" stroke="#0355a3" stroke-width="6" stroke-linecap="round"/></svg>
    Search Engine Marketing and Optimization
  </div>
  <div class="service" style="left:770px;top:154px">
    <svg width="124" height="124" viewBox="0 0 124 124"><path d="M62 4 A58 58 0 0 0 62 120" fill="none" stroke="#0355a3" stroke-width="6" stroke-dasharray="8 6"/><path d="M62 4 A58 58 0 0 1 62 120" fill="none" stroke="#666" stroke-width="5"/><path d="M42 66 a10 10 0 0 1 4-19 a14 14 0 0 1 27-3 a11 11 0 0 1 8 22 z" fill="none" stroke="#0355a3" stroke-width="3"/><rect x="52" y="68" width="8" height="8" fill="#0355a3"/><rect x="64" y="68" width="8" height="8" fill="#0355a3"/><circle cx="62" cy="84" r="4" fill="#0355a3"/></svg>
    Social Media Marketing
  </div>
  <div class="service" style="left:126px;top:418px">
    <svg width="124" height="124" viewBox="0 0 124 124"><path d="M62 4 A58 58 0 0 0 62 120" fill="none" stroke="#0355a3" stroke-width="6" stroke-dasharray="8 6"/><path d="M62 4 A58 58 0 0 1 62 120" fill="none" stroke="#666" stroke-width="5"/><circle cx="62" cy="60" r="12" fill="none" stroke="#0355a3" stroke-width="3"/><path d="M62 48 v-12 M50 60 h-12 M74 60 h12 M54 70 l-10 12 M70 70 l10 12 M62 72 v14" stroke="#0355a3" stroke-width="3"/></svg>
    Growth Hacking
  </div>
  <div class="service" style="left:450px;top:418px">
    <svg width="124" height="124" viewBox="0 0 124 124"><path d="M62 4 A58 58 0 0 0 62 120" fill="none" stroke="#0355a3" stroke-width="6" stroke-dasharray="8 6"/><path d="M62 4 A58 58 0 0 1 62 120" fill="none" stroke="#666" stroke-width="5"/><line x1="42" y1="82" x2="80" y2="42" stroke="#0355a3" stroke-width="7" stroke-linecap="round"/><line x1="44" y1="44" x2="80" y2="80" stroke="#0355a3" stroke-width="5" stroke-linecap="round"/></svg>
    Website Design
  </div>
  <div class="service" style="left:770px;top:418px">
    <svg width="124" height="124" viewBox="0 0 124 124"><path d="M62 4 A58 58 0 0 0 62 120" fill="none" stroke="#0355a3" stroke-width="6" stroke-dasharray="8 6"/><path d="M62 4 A58 58 0 0 1 62 120" fill="none" stroke="#666" stroke-width="5"/><rect x="48" y="38" width="26" height="34" fill="#fff" stroke="#0355a3" stroke-width="3"/><rect x="54" y="46" width="26" height="34" fill="#fff" stroke="#0355a3" stroke-width="3"/><path d="M59 56 h16 M59 63 h16 M59 70 h12" stroke="#0355a3" stroke-width="2"/></svg>
    Content &amp; Email Marketing
  </div>
</section>

<section class="trust abs">
  <h2 class="section-title centered-title" style="top:62px"><b>Why</b> Customers Trust Us</h2>
  <div class="dotted-rule" style="top:116px"></div>

  <div class="trust-item" style="left:145px;top:166px">
    <span class="trust-icon"><svg width="28" height="28" viewBox="0 0 28 28"><circle cx="21" cy="6" r="4" fill="#fff"/><circle cx="7" cy="14" r="4" fill="#fff"/><circle cx="21" cy="22" r="4" fill="#fff"/><path d="M7 14 L21 6 M7 14 L21 22" stroke="#fff" stroke-width="2"/></svg></span>
    <div><h3>Flexibility</h3><p>We adapt the campaign and strategy according to your workload, capacity and seasonality</p></div>
  </div>
  <div class="trust-item" style="left:624px;top:166px">
    <span class="trust-icon"><svg width="30" height="30" viewBox="0 0 30 30"><circle cx="15" cy="15" r="12" fill="none" stroke="#fff" stroke-width="2.5"/><path d="M10 10 L20 20 M20 10 L10 20" stroke="#fff" stroke-width="2.5"/></svg></span>
    <div><h3>No Annual Contracts</h3><p>We define a roadmap but only bill month to month</p></div>
  </div>
  <div class="trust-item" style="left:145px;top:270px">
    <span class="trust-icon"><svg width="28" height="28" viewBox="0 0 28 28"><rect x="4" y="4" width="6" height="12" fill="#fff"/><path d="M12 4 h10 l2 10 h-8 l1 10 h-3 l-2-8 v-12 z" fill="#fff"/></svg></span>
    <div><h3>No Set-Up Costs</h3><p>No fees are charged to set up web marketing campaigns. That's how confident we are in our ability to deliver results.</p></div>
  </div>
  <div class="trust-item" style="left:624px;top:270px">
    <span class="trust-icon"><svg width="30" height="30" viewBox="0 0 30 30"><circle cx="15" cy="15" r="12" fill="none" stroke="#fff" stroke-width="2.5"/><text x="15" y="21" text-anchor="middle" font-family="Open Sans, sans-serif" font-size="17" font-weight="700" fill="#fff">$</text></svg></span>
    <div><h3>Return on Investment</h3><p>We Calculate Your Campaign ROI on a weekly basis &amp; make sure you get the most out of every dollar spent</p></div>
  </div>
  <div class="trust-item" style="left:145px;top:372px">
    <span class="trust-icon"><svg width="30" height="30" viewBox="0 0 30 30"><path d="M15 3 L27 26 H3 Z" fill="none" stroke="#fff" stroke-width="2.5"/><path d="M11 20 L15 11 L19 20 M12.5 17 h5" stroke="#fff" stroke-width="2" fill="none"/></svg></span>
    <div><h3>Continuous Improvement</h3><p>Once your strategy is up and running, we thrive to optimize it and continuously improve results.</p></div>
  </div>
  <div class="trust-item" style="left:624px;top:372px">
    <span class="trust-icon"><svg width="28" height="28" viewBox="0 0 28 28"><path d="M6 3 l5 0 l2 6 l-3 3 a14 14 0 0 0 6 6 l3-3 l6 2 v5 a3 3 0 0 1-3 3 A21 21 0 0 1 3 6 a3 3 0 0 1 3-3z" fill="#fff"/></svg></span>
    <div><h3>Effective Communication</h3><p>We believe communication is key to both understanding your business goals, &amp; delivering them the right way.</p></div>
  </div>
</section>

<section class="approach abs">
  <div class="approach-copy">
    <p class="lead">Many IT companies can offer some kind of systems expertise, but with our approach, Lorbex IT can offer more:</p>
    <ul>
      <li>We are curious about your whole-business strategy. Our recommendations flow from the insight you provide about the future you are trying to create for your company.</li>
      <li>We have staggering options.<br>As a global company, we have access to thousands of vendors, products, managed services, and configurations. Lorbex IT offers real choice.</li>
      <li>We take a holistic approach.<br>We use technology to address initiatives, then execute with products, services, and flexible consumption models to deliver results.</li>
    </ul>
  </div>
  <div class="approach-photo" role="img" aria-label="Businessman viewed from behind facing a wall of sketched business charts"></div>
  <a class="btn-outline">CONTACT US</a>
</section>

<section class="contact abs">
  <h2>CONTACT US</h2>
  <div class="field" style="left:145px;top:98px;width:207px;height:44px">Name</div>
  <div class="field" style="left:366px;top:98px;width:208px;height:44px">Email Address</div>
  <div class="field" style="left:145px;top:156px;width:429px;height:128px">Message</div>
  <span class="captcha">9 + 11 =</span>
  <span class="captcha-box"></span>
  <a class="submit">Submit</a>

  <div class="testimonial">
    <span class="quote-mark">“</span>
    <span class="avatar" role="img" aria-label="Portrait of the company CEO"></span>
    <blockquote>“Our <b>Korvel Professional Services</b> will help you to convert web visitors into customers and provide cutting edge to grow your business”</blockquote>
    <cite><b>Mr. Denholm</b><br>CEO, Korvel Pro</cite>
  </div>
</section>

<footer class="site-footer abs">
  <div class="social"><span></span><span></span><span></span><span></span></div>
</footer>

</body>
</html>
```